Bus. Card/Envelope/Letterhead Design Request with my Logo

I have a logo created. I need to create a business card design, letterhead design and envelope design with the new logo.
Updates

The logo has now been posted. Thank you.

Target Market(s)

Professional. Legal Field.

Industry/Entity Type

Business

Requirements
Must have
• I like the same font as the logo.

```html
<!DOCTYPE html>
<html lang="en">
<head>
<meta charset="utf-8">
<title>Brannigan Kearney LLP – Business Card</title>
<link href="https://fonts.googleapis.com/css2?family=Cinzel:wght@400;500&family=Lato:wght@400&family=Arimo:wght@400&display=swap" rel="stylesheet">
<style>
  :root {
    --card-green: #72dd00;
    --brand-green: #66cc1a;
    --ink: #111111;
    --rule: #161616;
    --white: #ffffff;
    --muted: #7a7a7a;
    --frame: #222222;
    --hairline: #e2e2e2;
    --page: #ffffff;
  }
  html, body {
    margin: 0;
    padding: 0;
    overflow: hidden;
    background: var(--page);
  }
  .canvas {
    position: relative;
    width: 1200px;
    height: 475px;
    overflow: hidden;
    background: var(--page);
  }
  .side-label {
    position: absolute;
    top: -6px;
    margin: 0;
    font-family: "Arimo", Arial, sans-serif;
    font-weight: 400;
    font-size: 45px;
    color: var(--ink);
    transform: translateX(-50%);
    white-space: nowrap;
  }
  .side-label--front { left: 295px; }
  .side-label--back { left: 913px; }
  .presentation-frame {
    position: absolute;
    left: 1px;
    top: 48px;
    width: 1196px;
    height: 424px;
    border: 1px solid var(--frame);
  }

  /* Front card */
  .card-front {
    position: absolute;
    left: 51px;
    top: 100px;
    width: 533px;
    height: 332px;
    background: var(--card-green);
  }
  .front-mark {
    position: absolute;
    left: 242px;
    top: 106px;
    width: 50px;
    height: 50px;
    border-radius: 50%;
    background: var(--white);
  }
  .front-rule {
    position: absolute;
    left: 31px;
    width: 471px;
    height: 4px;
    background: var(--rule);
  }
  .front-rule--top { top: 153px; }
  .front-rule--bottom { top: 226px; }
  .firm-name {
    position: absolute;
    left: 0;
    top: 163px;
    width: 533px;
    margin: 0;
    text-align: center;
    font-family: "Cinzel", "Times New Roman", serif;
    font-weight: 400;
    font-size: 37px;
    letter-spacing: 1px;
    color: var(--white);
    white-space: nowrap;
  }
  .firm-tagline {
    position: absolute;
    left: 0;
    top: 245px;
    width: 533px;
    display: flex;
    justify-content: center;
    align-items: center;
    gap: 20px;
  }
  .firm-tagline__line {
    width: 46px;
    height: 1px;
    background: var(--rule);
  }
  .firm-tagline__text {
    font-family: "Cinzel", "Times New Roman", serif;
    font-size: 14px;
    letter-spacing: 6px;
    color: var(--ink);
    white-space: nowrap;
  }

  /* Back card */
  .card-back {
    position: absolute;
    left: 584px;
    top: 100px;
    width: 533px;
    height: 331px;
    background: var(--white);
    border: 1px solid var(--hairline);
    border-left: none;
  }
  .back-brand {
    position: absolute;
    left: 22px;
    top: 36px;
    display: flex;
    align-items: center;
    gap: 10px;
    font-family: "Cinzel", "Times New Roman", serif;
    font-size: 20px;
    color: var(--brand-green);
    white-space: nowrap;
  }
  .back-brand__dot {
    width: 40px;
    height: 40px;
    border-radius: 50%;
    background: var(--brand-green);
  }
  .holder-name {
    position: absolute;
    left: 43px;
    top: 128px;
    margin: 0;
    font-family: "Cinzel", "Times New Roman", serif;
    font-weight: 400;
    font-size: 30px;
    color: var(--brand-green);
  }
  .holder-role {
    position: absolute;
    left: 42px;
    top: 172px;
    margin: 0;
    font-family: "Lato", Arial, sans-serif;
    font-size: 20px;
    color: var(--ink);
  }
  .contact-list {
    position: absolute;
    left: 271px;
    top: 169px;
    margin: 0;
    padding: 0;
    list-style: none;
    font-family: "Lato", Arial, sans-serif;
    font-size: 15.5px;
    line-height: 20.5px;
    color: var(--muted);
    white-space: nowrap;
  }
  .office-address {
    position: absolute;
    left: 0;
    top: 282px;
    width: 533px;
    margin: 0;
    text-align: center;
    font-family: "Lato", Arial, sans-serif;
    font-size: 16px;
    color: var(--muted);
  }
</style>
</head>
<body>
<main class="canvas">
  <h2 class="side-label side-label--front">Front card</h2>
  <h2 class="side-label side-label--back">Back card</h2>
  <div class="presentation-frame"></div>

  <section class="card-front" aria-label="Front of business card">
    <div class="front-mark"></div>
    <div class="front-rule front-rule--top"></div>
    <h1 class="firm-name">Brannigan Kearney llp</h1>
    <div class="front-rule front-rule--bottom"></div>
    <div class="firm-tagline">
      <span class="firm-tagline__line"></span>
      <span class="firm-tagline__text">ATTORNEYS AT LAW</span>
      <span class="firm-tagline__line"></span>
    </div>
  </section>

  <section class="card-back" aria-label="Back of business card">
    <div class="back-brand"><span class="back-brand__dot"></span>Brannigan Kearney</div>
    <p class="holder-name">NAME</p>
    <p class="holder-role">DESIGNATION</p>
    <ul class="contact-list">
      <li>oxoxoxoxoxoxoxo : Phone</li>
      <li>xoxoxoxoxoxoxox :</li>
      <li>abcdefgh@brannigan.com</li>
      <li>www.examplesiteaddress.com</li>
    </ul>
    <p class="office-address">This the space for address, not the actual content</p>
  </section>
</main>
</body>
</html>
```